Home loan promotion flyer (DL or Postcard)

We need a flyer that promotes our home loan broking service. In summary, we are an Australian financial planning business that helps Gen X and Y make better financial planning decisions.

We would like the design to have a similar look and feel to the following:
http://www.leaflet-hub.com.au/kpwt/steady_path_brighter_days/

Text that I would like included is:

(HEADING) Awesome Debt Management: Someone else's money used to Your advantage.

(Paragraph) Debt is not necessarily a dirty work. Smart Australian investors often use debt strategies to minimise tax burdens, pay off their home loan sooner and to build their wealth quicker.

(Promotion) Bring this along to your COMPLIMENTARY finance health check and we will give you a $25 Brandt Halvey voucher to celebrate your first step towards a better financial future. (Please include the image of the voucher near this text).

Finally, you must include our number (1300 472 916) and website (www.kpwt.com.au)

Apart from being consistent with the e-brochure above (please ensure you view the link), we would like the design to be bold and stand out from the crowd.

I have attached a previous home loan promotion design that I like but I feel that there are too many words and not enough space. Please use the good elements but avoid the rest.

Finally, I've also attached a DL "goldfish" design that I really like because I think the design is memorable and stands-out.
Updates

Project Deadline Extended
Reason: Hi there designers Thanks for your designs so far. They look great. I have extended the brief to give everyone the opportunity to reassess their design to make sure that it is consistent with the design brief. If anything is unclear please don't hesitate to make contact. Thanks RL

Target Market(s)

Australian first home buyers and property investors.

Industry/Entity Type

Financial

Requirements
Must have
• The design MUST be consistent with the existing marketing material referred to in this link.

```html
<!DOCTYPE html>
<html lang="en">
<head>
<meta charset="utf-8">
<title>Keystone Path Wealth – Awesome Debt Management</title>
<link rel="stylesheet" href="https://fonts.googleapis.com/css2?family=Bitter:wght@400&family=Mulish:wght@400;600;700;800&display=swap">
<style>
  :root {
    --purple-deep: #4e1c60;
    --purple-mid: #74308a;
    --purple-light: #9a4bb0;
    --lime: #8ee53f;
    --lime-bright: #7ddc2a;
    --ink: #0b0b0b;
    --white: #ffffff;
    --text-dark: #141414;
  }
  * { margin: 0; padding: 0; box-sizing: border-box; }
  html, body { width: 1200px; height: 583px; overflow: hidden; background: #fff; }
  .flyer {
    position: relative;
    width: 1200px;
    height: 583px;
    overflow: hidden;
    font-family: "Mulish", Arial, sans-serif;
  }
  .hero-photo {
    position: absolute;
    inset: 0 240px 0 0;
    background: linear-gradient(100deg, var(--purple-deep) 0%, var(--purple-mid) 50%, var(--purple-light) 100%);
  }
  .side-panel {
    position: absolute;
    top: 0; left: 0;
    width: 1200px; height: 583px;
  }
  .message-box {
    position: absolute;
    left: 315px; top: 70px;
    width: 593px; height: 238px;
    background: var(--lime);
    border-radius: 3px;
    padding: 12px 24px 0 24px;
  }
  .message-box::before,
  .offer-box::before {
    content: "";
    position: absolute;
    left: -9px; top: 8px;
    border-top: 9px solid transparent;
    border-bottom: 9px solid transparent;
  }
  .message-box::before { border-right: 9px solid var(--lime); }
  .offer-box::before { border-right: 9px solid var(--ink); }
  .headline {
    font-family: "Bitter", Georgia, serif;
    font-weight: 400;
    color: var(--white);
    font-size: 34px;
    line-height: 1.0;
    white-space: nowrap;
  }
  .subheadline {
    font-family: "Bitter", Georgia, serif;
    font-weight: 400;
    color: var(--white);
    font-size: 20.5px;
    line-height: 1.2;
    margin: 2px 0 8px;
    white-space: nowrap;
  }
  .intro {
    color: var(--text-dark);
    font-weight: 600;
    font-size: 20.5px;
    line-height: 30px;
  }
  .line {
    display: block;
    text-align: justify;
    text-align-last: justify;
    white-space: nowrap;
  }
  .line:last-child { text-align-last: left; }
  .offer-box {
    position: absolute;
    left: 393px; top: 354px;
    width: 515px; height: 168px;
    background: var(--ink);
    border-radius: 4px;
    padding: 15px 20px 0 24px;
    color: var(--white);
    font-size: 20.5px;
    line-height: 29.5px;
  }
  .offer-highlight { color: var(--lime); }
  .brand {
    position: absolute;
    left: 995px; top: 58px;
    width: 180px;
    text-align: center;
    color: var(--white);
  }
  .brand-mark {
    display: block;
    width: 110px; height: 110px;
    margin: 0 auto 20px;
    background: var(--lime-bright);
    border-radius: 6px;
  }
  .brand-name {
    font-weight: 800;
    font-size: 24px;
    line-height: 1.1;
  }
  .social-links {
    position: absolute;
    left: 1014px; top: 444px;
    display: flex;
    gap: 30px;
  }
  .social-links span {
    width: 22px; height: 22px;
    background: var(--white);
    border-radius: 3px;
  }
  .contact {
    position: absolute;
    left: 963px; top: 480px;
    width: 240px;
    text-align: center;
    color: var(--white);
    font-style: normal;
    font-weight: 800;
    font-size: 21px;
    line-height: 37px;
  }
</style>
</head>
<body>
<main class="flyer">
  <div class="hero-photo" role="img" aria-label="Green ceramic piggy bank with a sunflower growing out of its coin slot, set on a purple backdrop"></div>

  <svg class="side-panel" viewBox="0 0 1200 583" aria-hidden="true">
    <path d="M946 0 H1200 V583 H868 Q946 570 946 490 Z" fill="var(--lime-bright)"/>
    <path d="M961 0 H1200 V583 H896 Q961 568 961 496 Z" fill="var(--ink)"/>
  </svg>

  <section class="message-box">
    <h1 class="headline">Awesome Debt Management:</h1>
    <p class="subheadline">Someone else's money used to Your advantage.</p>
    <p class="intro">
      <span class="line">Debt is not necessarily a dirty work. Smart Austra-</span>
      <span class="line">lian investors often use debt strategies to minimise</span>
      <span class="line">tax burdens, pay off their home loan sooner and to</span>
      <span class="line">build their wealth quicker.</span>
    </p>
  </section>

  <section class="offer-box">
    <p>
      <span class="line">Bring this along to your <span class="offer-highlight">COMPLIMENTARY</span></span>
      <span class="line">finance health check and we will give you a</span>
      <span class="line">$25 Brandt Halvey voucher to celebrate your</span>
      <span class="line">first step towards a better financial future.</span>
    </p>
  </section>

  <div class="brand">
    <span class="brand-mark"></span>
    <p class="brand-name">Keystone Path Wealth</p>
  </div>

  <div class="social-links" aria-hidden="true">
    <span></span><span></span><span></span>
  </div>

  <address class="contact">
    <p>1300 472 916</p>
    <p>www.kpwt.com.au</p>
  </address>
</main>
</body>
</html>
```